Easy Marinade Labels for Butchery Store

Need a set of labels designed for a Butchery Shop. They will sit in the top left corner of the packets as a triangle (7cm each side). Easy because the only major requirement is the label name and some small text saying "Please ask in store to see spec sheet for ingredients". Extra points for finding a fun way to incorporate the logo and/or images of food (garlic bulbs, chilli, spices ect) to enhance the label. List of Marinade Names below: GarlicPepper Mint & RosemarySatayBBQChilli Plum & GingerSundried Tomato & BasilBuffaloHoney SoyHoi-SinPer PeriSpicy CajunTeriyakiBlack Bean Ive also attached the logo and an example of how the label might sit on a packet of meat. Thanks

Target Market(s)

Butchery Deli Shop Customers

Industry/Entity Type

Food Store

Font styles to use
Serif
Sans Serif
Decorative
Other font styles liked:
• Fun font that isn't a generic Quillbrenn Font?

Colors

Designer to choose colors to be used in the design.

Requirements
Must have
• Product Name
• Small text saying "Please ask in store to see spec sheet for ingredients"
Nice to have
• Photos of ingredients that would match that type of marinade - Chilli, Garlic, Spices.
• Tavo Crest Logo - not essential if it doesn't look good on the label / doesn't fit.

```html
<!DOCTYPE html>
<html lang="en">
<head>
<meta charset="utf-8">
<title>Tavo Crest Marinade Label</title>
<link rel="stylesheet" href="https://fonts.googleapis.com/css2?family=Oswald:wght@400;600&display=swap">
<style>
  :root {
    --red-deep: #a81414;
    --red-bright: #f20f0f;
    --ink: #0c0c0c;
    --rule: #5a0a0a;
    --yellow: #ffd21a;
    --white: #ffffff;
    --ingredient-light: #f1e7dc;
    --ingredient-red: #c8102e;
  }
  html, body {
    margin: 0;
    padding: 0;
    width: 1200px;
    height: 1200px;
    overflow: hidden;
    background: var(--white);
  }
  .label-canvas {
    display: block;
    width: 1200px;
    height: 1200px;
  }
  .flavour-names {
    font-family: "Oswald", sans-serif;
    font-weight: 600;
    font-size: 13px;
    fill: var(--yellow);
    letter-spacing: 0.3px;
  }
  .notice-text {
    font-family: "Oswald", sans-serif;
    font-weight: 400;
    font-size: 24px;
    fill: var(--white);
  }
  .brand-name {
    font-family: "Oswald", sans-serif;
    font-weight: 600;
    font-size: 30px;
    fill: var(--red-deep);
  }
</style>
</head>
<body>
<svg class="label-canvas" viewBox="0 0 827 827" xmlns="http://www.w3.org/2000/svg">
  <defs>
    <linearGradient id="label-red" x1="0" y1="0" x2="0.5" y2="0.5">
      <stop offset="0" stop-color="var(--red-deep)"/>
      <stop offset="1" stop-color="var(--red-bright)"/>
    </linearGradient>
    <radialGradient id="ingredient-tones" cx="0.55" cy="0.4" r="0.6">
      <stop offset="0" stop-color="var(--ingredient-light)"/>
      <stop offset="0.55" stop-color="#e9c9b4"/>
      <stop offset="1" stop-color="var(--ingredient-red)" stop-opacity="0.85"/>
    </radialGradient>
  </defs>

  <polygon class="label-triangle" points="0,0 827,0 0,827" fill="url(#label-red)"/>

  <g class="brand-plate" transform="rotate(-22 105 88)">
    <rect x="14" y="34" width="182" height="108" fill="var(--white)"/>
    <text class="brand-name" x="105" y="99" text-anchor="middle">Tavo Crest</text>
  </g>

  <ellipse class="ingredient-art" role="img" aria-label="Garlic bulb with cloves, parsley leaf and red chillies"
           cx="230" cy="222" rx="165" ry="108" fill="url(#ingredient-tones)" opacity="0.9"/>

  <g class="diagonal-band" transform="translate(370 358) rotate(-43)">
    <text class="flavour-names" x="-20" y="-58" text-anchor="middle">GARLIC PEPPER MINT &amp;</text>
    <text class="flavour-names" x="-20" y="-44" text-anchor="middle">ROSEMARYSATAY BBQCHILLI PLUM</text>

    <line class="band-rule" x1="-300" y1="-38" x2="250" y2="-38" stroke="var(--rule)" stroke-width="1"/>

    <polygon class="ribbon-tail" points="-340,4 -285,4 -285,54 -340,54 -325,29" fill="var(--ink)"/>
    <polygon class="ribbon-tail" points="340,4 285,4 285,54 340,54 325,29" fill="var(--ink)"/>
    <polygon class="ribbon-fold" points="-300,30 -285,30 -285,54" fill="#000"/>
    <polygon class="ribbon-fold" points="300,30 285,30 285,54" fill="#000"/>

    <rect class="notice-ribbon" x="-300" y="-30" width="600" height="60" fill="var(--ink)"/>
    <text class="notice-text" x="0" y="9" text-anchor="middle" textLength="556" lengthAdjust="spacingAndGlyphs">PLEASE ASK IN STORE TO SEE SPEC SHEET FOR INGREDIENTS</text>
  </g>
</svg>
</body>
</html>
```